Harbor Business Cards

I need a business card designed with the following information.

Company Name: Harbor Wealth Management
Name: BriAnne Dockery
Title: Executive Assistant
Cell: (281) 555-0173
Direct Line: (832) 555-0148
Email: brianne@harborwmx.com
Address: 20537 W. Marlowe PKWY Ste. B
Larkton, TY 77390

I have attached the logo.
I would like it in navy blue and silver.
Thanks.

```html
<!DOCTYPE html>
<html lang="en">
<head>
<meta charset="utf-8">
<title>BriAnne Dockery – Business Card</title>
<link href="https://fonts.googleapis.com/css2?family=Noto+Sans:wght@400;600&family=Roboto:wght@500&display=swap" rel="stylesheet">
<style>
  :root {
    --navy: #2b354a;
    --navy-band-top: #3e475b;
    --navy-band-bottom: #5b6377;
    --silver-top: #d5d6d9;
    --silver-bottom: #a9abb0;
    --silver-band: #9a9ca2;
    --light-text: #d3d4d6;
    --dark-text: #333c52;
    --white: #ffffff;
    --page: #ffffff;
  }
  * { margin: 0; padding: 0; box-sizing: border-box; }
  html, body { width: 1200px; height: 1200px; overflow: hidden; background: var(--page); }
  .canvas { position: relative; width: 1200px; height: 1200px; }

  .card { position: absolute; left: 271px; width: 659px; height: 378px; overflow: hidden; }
  .card--front { top: 212px; background: var(--navy); color: var(--light-text); }
  .card--back { top: 611px; background: linear-gradient(180deg, var(--silver-top) 0%, var(--silver-bottom) 100%); color: var(--dark-text); }

  .card__emblem-area { position: absolute; top: 80px; width: 300px; height: 235px; }
  .card--front .card__emblem-area {
    left: 0;
    background: radial-gradient(ellipse at 35% 85%, rgba(255,255,255,0.14) 0%, rgba(255,255,255,0.06) 45%, rgba(255,255,255,0) 75%);
  }
  .card--back .card__emblem-area {
    right: 0;
    background: radial-gradient(ellipse at 65% 85%, rgba(60,68,88,0.22) 0%, rgba(60,68,88,0.08) 45%, rgba(60,68,88,0) 75%);
  }

  .card__band { position: absolute; left: 0; top: 315px; width: 100%; height: 49px; }
  .card--front .card__band { background: linear-gradient(180deg, var(--navy-band-top), var(--navy-band-bottom)); }
  .card--back .card__band { background: var(--silver-band); opacity: 0.75; }
  .card__rule-bottom { position: absolute; left: 0; top: 364px; width: 100%; height: 1px; background: var(--white); }

  .card__identity { position: absolute; top: 48px; width: 310px; text-align: center; }
  .card--front .card__identity { left: 334px; }
  .card--back .card__identity { left: 15px; }
  .card__name { font-family: "Noto Sans", sans-serif; font-weight: 600; font-size: 37px; line-height: 56px; white-space: nowrap; }
  .card__divider { height: 2px; margin-top: 1px; }
  .card--front .card__divider { background: var(--light-text); }
  .card--back .card__divider { background: var(--dark-text); }
  .card__title { font-family: "Noto Sans", sans-serif; font-size: 19px; letter-spacing: 4.2px; margin-top: 3px; white-space: nowrap; }

  .card__contacts { position: absolute; top: 223px; font-family: "Roboto", sans-serif; font-weight: 500; }
  .card--front .card__contacts { left: 341px; color: var(--white); }
  .card--back .card__contacts { left: 22px; }
  .contact-row { display: flex; align-items: center; height: 32px; font-size: 14.5px; white-space: nowrap; }
  .contact-row__icon { width: 19px; height: 19px; margin-right: 7px; flex: none; }
  .contact-row__at { width: 19px; font-size: 20px; margin-right: 6px; line-height: 1; }
  .contact-address { font-size: 12.3px; margin-top: 5px; letter-spacing: 0.1px; white-space: nowrap; }
</style>
</head>
<body>
<div class="canvas">

  <section class="card card--front">
    <div class="card__emblem-area" role="img" aria-label="Faint brand emblem decoration"></div>
    <div class="card__band"></div>
    <div class="card__rule-bottom"></div>
    <div class="card__identity">
      <h1 class="card__name">BriAnne Dockery</h1>
      <div class="card__divider"></div>
      <p class="card__title">Executive Assistant</p>
    </div>
    <div class="card__contacts">
      <div class="contact-row">
        <svg class="contact-row__icon" viewBox="0 0 20 20" fill="none" stroke="currentColor" stroke-width="1.4"><circle cx="10" cy="10" r="8.5"/><path d="M7 5.5l1.6 2.2-1 1.2c.7 1.4 1.7 2.4 3.1 3.1l1.2-1 2.2 1.6-.9 1.6c-3.6-.4-6.5-3.3-6.9-6.9z"/></svg>
        <span>(281) 555 - 0173 - (832) 555 - 0148</span>
      </div>
      <div class="contact-row">
        <span class="contact-row__at">@</span>
        <span>brianne@harborwmx.com</span>
      </div>
      <p class="contact-address">20537 W. Marlowe PKWY Ste. B Larkton, TY 77390</p>
    </div>
  </section>

  <section class="card card--back">
    <div class="card__emblem-area" role="img" aria-label="Faint brand emblem decoration"></div>
    <div class="card__band"></div>
    <div class="card__rule-bottom"></div>
    <div class="card__identity">
      <h2 class="card__name">BriAnne Dockery</h2>
      <div class="card__divider"></div>
      <p class="card__title">Executive Assistant</p>
    </div>
    <div class="card__contacts">
      <div class="contact-row">
        <svg class="contact-row__icon" viewBox="0 0 20 20" fill="none" stroke="currentColor" stroke-width="1.4"><circle cx="10" cy="10" r="8.5"/><path d="M7 5.5l1.6 2.2-1 1.2c.7 1.4 1.7 2.4 3.1 3.1l1.2-1 2.2 1.6-.9 1.6c-3.6-.4-6.5-3.3-6.9-6.9z"/></svg>
        <span>(281) 555 - 0173 - (832) 555 - 0148</span>
      </div>
      <div class="contact-row">
        <span class="contact-row__at">@</span>
        <span>brianne@harborwmx.com</span>
      </div>
      <p class="contact-address">20537 W. Marlowe PKWY Ste. B Larkton, TY 77390</p>
    </div>
  </section>

</div>
</body>
</html>
```